Career development coaching - school lever to adults, needs a business card

Tandem Lark - An independent Career Advice business that provides 1-2-1 advice,for career development, entrepreneurial support and workshops needs a business card. Our clients of all ages (school leaver to adults looking for a career move) and universities and colleges. We would like the card to be double-sided with a modern, professional look. Looking for something professional yet very creative and original. Want a standard size business card that inspires a second look because it stands out from the rest.

One side of the card to have a design incorporating the logo with Tandem Lark name with the strap line “Guiding every next step ahead” and space for the company website

Other side of the card to the logo/Tandem Lark name and the usual contact information:
Individual Name
Job Title (for example, Director)
Phone number
Email address
Company website address

Facebook, LinkedIn and Twitter links will need to go somewhere (back or front!)

The design will be used for 3 individuals so should be editable so that we can update as needed/as we grow.

Attached is the company logo/colours to be incorporated.

Target Market(s)

1-2-1 advice,for career development, entrepreneurial support and workshops needs a business card. Our clients of all ages (school leaver to adults looking for a career move) and universities and colleges.

Industry/Entity Type

Consulting

Contact Information for Business Card

Individual Name
Phone number
Email address
Company website address

Font styles to use
Sans Serif

Colors
0255a3
3176b5
faa54b
f78f20
85acd3
cfdeed

Requirements
Must have
• use the Tandem Lark Logo in some way - using the colours and the blue/orange palette
• For the logo - hope this makes sense to someone or if they direclty relate to the logo image attached!
• For the Orange:- Pantone 1585 C
• In CMYK : C3 M71 Y100 K0
• For the Blue:- 100% Pantone 7469 C
• In CMYK : C100 M62 Y27 K7
• Please feel free to contact me with any questions for more info
Nice to have
• happy to see any creative designs
Should not have
• Nothing too traditional,

```html
<!DOCTYPE html>
<html lang="en">
<head>
<meta charset="utf-8">
<title>Tandem Lark – Business Card</title>
<link rel="stylesheet" href="https://fonts.googleapis.com/css2?family=Montserrat:wght@400;500;600&family=Alegreya:wght@500&display=swap">
<style>
  :root {
    --blue: #0255a3;
    --blue-mid: #3176b5;
    --orange: #f78f20;
    --orange-deep: #ec6f22;
    --card: #ffffff;
    --ink: #1f1f1f;
    --stage: #2e2e2e;
  }
  * { box-sizing: border-box; margin: 0; padding: 0; }
  html, body { width: 1200px; height: 900px; overflow: hidden; }
  body {
    background: var(--stage);
    position: relative;
    font-family: "Montserrat", sans-serif;
  }
  .card {
    position: absolute;
    width: 700px;
    height: 400px;
    background: var(--card);
    overflow: hidden;
    box-shadow: 0 10px 30px rgba(0,0,0,.45);
  }
  .card--back { left: 70px; top: 50px; }
  .card--front { left: 430px; top: 460px; }
  .card__accent {
    position: absolute; inset: 0; width: 700px; height: 400px;
  }
  .card__accent .band-main { fill: var(--orange-deep); }
  .card__accent .band-thin { fill: var(--orange); }

  /* front */
  .front-brand {
    position: absolute; left: 0; width: 560px; top: 110px;
    display: flex; flex-direction: column; align-items: center;
  }
  .brand-dot {
    width: 74px; height: 74px; border-radius: 50%;
    background: var(--blue); margin-bottom: 22px;
  }
  .brand-name {
    font-weight: 600; color: var(--blue);
    font-size: 50px; letter-spacing: 2px; text-transform: uppercase; line-height: 1;
  }
  .tagline {
    font-family: "Alegreya", serif; font-weight: 500;
    color: var(--blue); font-size: 30px; margin-top: 6px;
  }
  .web {
    color: var(--orange-deep); font-weight: 600; font-size: 20px;
    letter-spacing: 1px; margin-top: 12px;
  }

  /* back */
  .back-brand {
    position: absolute; left: 40px; top: 150px; width: 300px;
    display: flex; flex-direction: column; align-items: center;
  }
  .back-brand .brand-dot { width: 56px; height: 56px; margin-bottom: 16px; }
  .back-brand .brand-name { font-size: 30px; letter-spacing: 1px; }
  .back-brand .tagline { font-size: 19px; margin-top: 4px; }
  .social {
    display: flex; gap: 8px; margin-top: 26px; list-style: none;
  }
  .social li { width: 24px; height: 24px; background: var(--blue-mid); }
  .contact {
    position: absolute; left: 390px; top: 150px;
    color: var(--ink); font-size: 15px; line-height: 1.45;
  }
  .contact__name { font-weight: 600; }
  .contact__role { margin-bottom: 18px; }
</style>
</head>
<body>
  <section class="card card--back" aria-label="Business card, contact side">
    <svg class="card__accent" viewBox="0 0 700 400" aria-hidden="true">
      <polygon class="band-main" points="560,0 700,0 700,120"/>
      <polygon class="band-thin" points="620,400 700,320 700,400"/>
    </svg>
    <div class="back-brand">
      <div class="brand-dot"></div>
      <p class="brand-name">Tandem Lark</p>
      <p class="tagline">Guiding every next step ahead</p>
      <ul class="social" aria-label="Social links">
        <li></li><li></li><li></li>
      </ul>
    </div>
    <div class="contact">
      <p class="contact__name">Individual Name</p>
      <p class="contact__role">Director</p>
      <p>Ph: 555-0142-77</p>
      <p>E: info@tandemlark.com</p>
      <p>W: tandemlark.com</p>
    </div>
  </section>

  <section class="card card--front" aria-label="Business card, brand side">
    <svg class="card__accent" viewBox="0 0 700 400" aria-hidden="true">
      <rect class="band-main" x="640" y="0" width="60" height="400"/>
      <rect class="band-thin" x="620" y="0" width="10" height="400"/>
    </svg>
    <div class="front-brand">
      <div class="brand-dot"></div>
      <p class="brand-name">Tandem Lark</p>
      <p class="tagline">Guiding every next step ahead</p>
      <p class="web">www.tandemlark.com</p>
    </div>
  </section>
</body>
</html>
```